Energy trading company (Voltrisa) needs a business card

We need a business card for a company based in Central America. Our main purpose is trading energy . We already have the logo but we need some good creativity to design a high impact business card. Colors blue, orange, green can be used or we would like to see good combinatios with our logo

Target Market(s)

Energy

Industry/Entity Type

Power Generation

Contact Information for Business Card

Logo , headquarters , name, background

Font styles to use
Serif
Sans Serif

Colors

Designer to choose colors to be used in the design.

Requirements
Must have
• it must have a fresh and clean view
Nice to have
• good backgrounds that combine with the logo
Should not have
• too much words

```html
<!DOCTYPE html>
<html lang="en">
<head>
<meta charset="utf-8">
<title>Voltrisa Business Card</title>
<link href="https://fonts.googleapis.com/css2?family=Source+Sans+3:wght@300;400;600;900&display=swap" rel="stylesheet">
<style>
  :root {
    --orange-warm: #f05a22;
    --orange-gold: #e8860c;
    --ink: #111111;
    --paper: #f4f4f2;
    --stage: #a3a3a3;
    --rule: #555555;
  }
  * { box-sizing: border-box; margin: 0; padding: 0; }
  html, body { width: 1200px; height: 720px; overflow: hidden; }
  body {
    background: var(--stage);
    font-family: "Source Sans 3", sans-serif;
    display: flex; align-items: center; justify-content: center; gap: 40px;
  }
  .card {
    width: 540px; height: 309px; position: relative;
    box-shadow: 0 6px 18px rgba(0,0,0,.25);
  }
  .card-front {
    background: linear-gradient(135deg, var(--orange-warm), var(--orange-gold));
    display: flex; align-items: center; justify-content: center;
  }
  .wordmark { display: flex; align-items: center; gap: 12px; font-weight: 400; letter-spacing: .04em; }
  .wordmark-dot { border-radius: 50%; }
  .card-front .wordmark { color: #fff; font-size: 56px; }
  .card-front .wordmark-dot { width: 34px; height: 34px; background: #fff; }
  .card-back { background: var(--paper); }
  .card-back .wordmark {
    position: absolute; left: 30px; top: 128px; color: var(--ink); font-size: 34px; gap: 8px;
  }
  .card-back .wordmark-dot { width: 22px; height: 22px; background: linear-gradient(135deg, var(--orange-warm), var(--orange-gold)); }
  .divider { position: absolute; left: 238px; width: 1.5px; height: 26px; background: var(--rule); }
  .divider-top { top: 0; }
  .divider-bottom { bottom: 0; }
  .contact { position: absolute; left: 262px; top: 52px; right: 20px; color: var(--ink); }
  .contact-name { font-weight: 900; font-size: 19px; }
  .contact-title { font-weight: 300; font-size: 15px; letter-spacing: .12em; margin-bottom: 14px; }
  .contact-row { display: flex; align-items: center; gap: 10px; font-size: 15px; font-weight: 300; margin-bottom: 8px; }
  .contact-icon { width: 26px; height: 26px; flex: none; }
  .contact-address { font-size: 15px; line-height: 1.25; margin-top: 12px; }
</style>
</head>
<body>
  <section class="card card-front" aria-label="Card front">
    <div class="wordmark"><span class="wordmark-dot"></span><span>VOLTRISA</span></div>
  </section>

  <section class="card card-back" aria-label="Card back">
    <div class="wordmark"><span class="wordmark-dot"></span><span>VOLTRISA</span></div>
    <span class="divider divider-top"></span>
    <span class="divider divider-bottom"></span>
    <div class="contact">
      <p class="contact-name">Dario Venturelli</p>
      <p class="contact-title">FOUNDER &amp; CEO</p>
      <p class="contact-row">
        <svg class="contact-icon" viewBox="0 0 26 26" aria-hidden="true">
          <defs><linearGradient id="badge" x1="0" y1="0" x2="1" y2="1"><stop offset="0" stop-color="#f05a22"/><stop offset="1" stop-color="#e8860c"/></linearGradient></defs>
          <circle cx="13" cy="13" r="12" fill="url(#badge)"/>
          <path d="M7 11c0-2 3-3 6-3s6 1 6 3l-2 1-1-1.5h-6L9 12zM9 13h8l1 5H8z" fill="#fff"/>
        </svg>
        555-741-2093
      </p>
      <p class="contact-row">
        <svg class="contact-icon" viewBox="0 0 26 26" aria-hidden="true">
          <circle cx="13" cy="13" r="12" fill="url(#badge)"/>
          <rect x="7" y="9" width="12" height="8" fill="none" stroke="#fff" stroke-width="1.5"/>
          <path d="M7 9l6 5 6-5" fill="none" stroke="#fff" stroke-width="1.5"/>
        </svg>
        dario@voltrisa.com.sv
      </p>
      <p class="contact-row">
        <svg class="contact-icon" viewBox="0 0 26 26" aria-hidden="true">
          <circle cx="13" cy="13" r="12" fill="url(#badge)"/>
          <circle cx="13" cy="13" r="6" fill="none" stroke="#fff" stroke-width="1.5"/>
          <path d="M7 13h12M13 7c-3 3-3 9 0 12M13 7c3 3 3 9 0 12" fill="none" stroke="#fff" stroke-width="1.2"/>
        </svg>
        www.voltrisa.com.sv
      </p>
      <p class="contact-address">Av. Las Palmas, Torre Norte 3b<br>Of 27-C, San Salvador</p>
    </div>
  </section>
</body>
</html>
```